KelVane Product Technical Information Brochure Template

We are looking to create a template that allows us to easily transfer our current brochures into the new brochure.
The new brochure should be professional & energetic, communicating the brand well.
the brochure template should include a:
• Front Cover: KelVane Logo, and area where we can insert a picture of the product, an area for text of the product name & model. Then, it should incorporate images that advertise out diversity in the Pharmaceutical, Nutraceutical, Food, Chemical, Bio, Health & Beauty
•Brochure Content: See sample brochure
• Back Cover: KelVane Logo, a global map, with list of offices in it and offices listed
I have included our product catalog as an example, as well as an ad that was recently made for examples only. Looking to take our design to the next level. I am also including competitors catalogs as example for ideas. BRANDING IS KEY.
We would like this in a template form as we have over 30 brochures to do. Our example brochure is in Word, however we can edit a PDF also if needed.
***Although we are requesting this in template format, winning designer will be asked for a price to complete all 28 brochures. If the price is good, we may consider just having this completed for us using these templates.***
Target Market(s)
Pharmaceutical, nutraceutical, food, bio, chemical, and health & beauty / cosmetics
Requirements
Must have
- •Focus on branding
•Show the diversity of our products, pharmaceutical/nutraceutical. food & beverage, chemical, bio, health & beauty/cosmetics
•Editable regions where we can edit text/content if needed.
Nice to have
- Category icons for
•Pharmaceutical/Nutraceutical
•Food
•Chemical
•Health & Beauty/Cosmetics
•Bio

```html
<!DOCTYPE html>
<html lang="en">
<head>
<meta charset="utf-8">
<title>KelVane – Specifications</title>
<link href="https://fonts.googleapis.com/css2?family=Arimo:wght@400;700&family=Montserrat:wght@300;400;600;800&display=swap" rel="stylesheet">
<style>
  :root {
    --navy: #0b4260;
    --red: #c62f3b;
    --panel-light: #eef7fc;
    --panel-deep: #d7eef6;
    --ink: #111;
    --note-ink: #44505a;
    --white: #fff;
  }
  * { margin: 0; padding: 0; box-sizing: border-box; }
  html, body { width: 927px; height: 1200px; overflow: hidden; background: var(--white); }
  .page { position: relative; width: 927px; height: 1200px; }

  .top-band { position: absolute; left: 84.5px; top: 0; width: 751.5px; height: 30px; background: var(--navy); }
  .top-stripe { position: absolute; left: 84.5px; top: 30px; width: 751.5px; height: 12px; background: var(--red); }

  .panel { position: absolute; left: 84.5px; top: 83.5px; width: 751.5px; height: 1022.5px; background: var(--panel-deep); overflow: hidden; }
  .panel-bg { position: absolute; inset: 0; width: 100%; height: 100%; }

  .title {
    position: absolute; left: 0; right: 0; top: 44px; text-align: center;
    font-family: "Montserrat", sans-serif; font-weight: 800; font-size: 29px;
    color: var(--red); letter-spacing: -0.3px;
  }

  .spec-table {
    position: absolute; left: 44.5px; top: 97px; width: 662.5px;
    border-collapse: collapse; table-layout: fixed;
    font-family: "Arimo", Arial, sans-serif; background: var(--white);
  }
  .spec-table col { width: 20%; }
  .spec-table th {
    background: var(--navy); color: var(--white); font-weight: 700; font-size: 12.3px;
    text-align: left; padding: 0 7.5px; height: 44.5px; line-height: 16px;
    border: 1px solid #0a2f45; border-right-color: #e6eef3;
  }
  .spec-table th:last-child { border-right-color: #0a2f45; }
  .spec-table td {
    color: var(--ink); font-size: 12.5px; padding: 0 7.5px; height: 22.6px;
    border: 1px solid #1b1b1b; line-height: 1;
  }

  .notes {
    position: absolute; left: 44.5px; top: 587px; width: 662.5px; list-style: none;
    font-family: "Montserrat", sans-serif; font-weight: 400; font-size: 13.4px;
    color: var(--note-ink); line-height: 18.5px;
  }
  .notes li { display: flex; margin-bottom: 10px; }
  .notes .num { width: 27px; flex: none; font-weight: 700; color: #1f2a33; }
  .notes .text { text-align: justify; letter-spacing: 0.15px; }

  .product-views { position: absolute; inset: 0; pointer-events: none; }
  .product-view {
    position: absolute; top: 821.5px; width: 155px; height: 155px; border-radius: 50%;
    border: 1.5px solid var(--navy);
    background: radial-gradient(circle at 50% 50%, #e4e8eb 0 30%, #c4ccd2 31% 36%, transparent 37%), transparent;
  }
  .view-1 { left: 44px; }
  .view-2 { left: 213.5px; }
  .view-3 { left: 383px; }
  .view-4 { left: 552.5px; }

  .footer {
    position: absolute; left: 84.5px; top: 1146px; width: 751.5px;
    font-family: "Montserrat", sans-serif; font-size: 13px; color: var(--navy);
    letter-spacing: 2.6px; display: flex; align-items: center;
  }
  .footer .sep { margin: 0 19px 0 22px; }
  .footer .page-no { margin-left: auto; letter-spacing: 2.4px; }
  .footer .page-no b { font-weight: 800; letter-spacing: 0; }

  .bottom-band { position: absolute; left: 84.5px; top: 1179px; width: 751.5px; height: 21px; background: var(--navy); }
</style>
</head>
<body>
<div class="page">
  <div class="top-band"></div>
  <div class="top-stripe"></div>

  <section class="panel">
    <svg class="panel-bg" viewBox="0 0 751.5 1022.5" preserveAspectRatio="none" aria-hidden="true">
      <polygon points="0,0 751.5,0 751.5,518 375,893 0,518" fill="#eef7fc"/>
    </svg>

    <h1 class="title">SPECIFICATIONS:</h1>

    <table class="spec-table">
      <colgroup><col><col><col><col><col></colgroup>
      <thead>
        <tr><th>Model</th><th>Total capacity<br>(liter)</th><th>Working capacity<br>(liter)</th><th>Power (*)<br>(kW)</th><th>Shaft Speed (RPM)</th></tr>
      </thead>
      <tbody>
        <tr><td>KVM-150</td><td>150</td><td>105</td><td>1.1 ~ 5</td><td>105</td></tr>
        <tr><td>KVM-300</td><td>300</td><td>210</td><td>3 ~ 8</td><td>83</td></tr>
        <tr><td>KVM-400</td><td>400</td><td>280</td><td>5 ~ 15</td><td>73</td></tr>
        <tr><td>KVM-500</td><td>500</td><td>350</td><td>7 ~ 21</td><td>66</td></tr>
        <tr><td>KVM-750</td><td>750</td><td>525</td><td>8 ~ 27</td><td>61</td></tr>
        <tr><td>KVM-1000</td><td>1000</td><td>700</td><td>12 ~ 40</td><td>52</td></tr>
        <tr><td>KVM-1500</td><td>1500</td><td>1050</td><td>14 ~ 48</td><td>48</td></tr>
        <tr><td>KVM-2000</td><td>2000</td><td>1400</td><td>19 ~ 64</td><td>42</td></tr>
        <tr><td>KVM-3000</td><td>3000</td><td>2100</td><td>22 ~ 78</td><td>38</td></tr>
        <tr><td>KVM-4000</td><td>4000</td><td>2800</td><td>29 ~ 101</td><td>33</td></tr>
        <tr><td>KVM-5000</td><td>5000</td><td>3500</td><td>34 ~ 120</td><td>30</td></tr>
        <tr><td>KVM-6000</td><td>6000</td><td>4200</td><td>34 ~ 120</td><td>30</td></tr>
        <tr><td>KVM-7000</td><td>7000</td><td>4900</td><td>38 ~ 137</td><td>28</td></tr>
        <tr><td>KVM-8000</td><td>8000</td><td>5600</td><td>43 ~ 153</td><td>26</td></tr>
        <tr><td>KVM-10000</td><td>10000</td><td>7000</td><td>47 ~ 167</td><td>25</td></tr>
        <tr><td>KVM-12000</td><td>12000</td><td>8400</td><td>50 ~ 180</td><td>24</td></tr>
        <tr><td>KVM-15000</td><td>15000</td><td>10500</td><td>57 ~ 205</td><td>22</td></tr>
        <tr><td>KVM-20000</td><td>20000</td><td>14000</td><td>63 ~ 227</td><td>21</td></tr>
      </tbody>
    </table>

    <ol class="notes">
      <li><span class="num">1.</span><span class="text">All specifications and illustrations are as accurate as is reasonably possible, but they are not binding.</span></li>
      <li><span class="num">2.</span><span class="text">KelVane reserves the right to modify the design without notice.</span></li>
    </ol>

    <div class="product-views">
      <div class="product-view view-1" role="img" aria-label="Stainless steel mixer with conical bottom and side motor, exterior view"></div>
      <div class="product-view view-2" role="img" aria-label="Mixer shown in cutaway revealing the internal screw agitator"></div>
      <div class="product-view view-3" role="img" aria-label="Mixer cutaway from a second angle showing the agitator"></div>
      <div class="product-view view-4" role="img" aria-label="Mixer vessel top view with drive motor and discharge valve"></div>
    </div>
  </section>

  <footer class="footer">
    <span>WWW.KELVANETEC.COM</span>
    <span class="sep">|</span>
    <span>WWW.KELVANE-MIXING.COM</span>
    <span class="page-no">PAGE &nbsp;| &nbsp;<b>4</b></span>
  </footer>

  <div class="bottom-band"></div>
</div>
</body>
</html>
```